Brovanix Stationery Design Project

We need a stationery design for our new business Brovanix which deals in advanced cleaning technologies such as Ultrasonic cleaning and high pressure cleaning machinery.

Our colour scheme is as per the included files.

We require business cards, letterheads, a brochure folder and email signatures design
Updates

Apologies for the delay in making a decision on this project. We will be making a final decision during the course of next week

Target Market(s)

Industries ranging from medical, automotive, mining, engineering all requiring specialised cleaning services

Industry/Entity Type

Pressure Cleaning

Requirements
Must have
• Please include our supplied logo and colour scheme. The design needs to be professional but creative.

```html
<!DOCTYPE html>
<html lang="en">
<head>
<meta charset="utf-8">
<title>Brovanix Stationery</title>
<link rel="stylesheet" href="https://fonts.googleapis.com/css2?family=Arimo:ital,wght@0,400;0,700;1,700&display=swap">
<style>
  :root {
    --backdrop: #d6d6d8;
    --paper: #ffffff;
    --sweep: #eeeff2;
    --sweep-soft: #f5f6f8;
    --brand-blue: #44569f;
    --brand-blue-deep: #34448a;
    --brand-blue-light: #5a6cb4;
    --ink: #3a3a3c;
    --muted: #8b8d93;
    --rule: #c9ccd3;
  }
  * { box-sizing: border-box; margin: 0; padding: 0; }
  html, body { width: 1200px; height: 800px; overflow: hidden; }
  body {
    background: var(--backdrop);
    font-family: "Arimo", Arial, sans-serif;
    color: var(--ink);
    position: relative;
  }
  .sheet {
    position: absolute;
    background: var(--paper);
    overflow: hidden;
    box-shadow: 0 2px 8px rgba(0,0,0,0.18);
  }
  .sheet > svg.art { position: absolute; inset: 0; width: 100%; height: 100%; }
  .sheet > *:not(.art) { position: absolute; }

  /* brand lockup */
  .brand { display: flex; align-items: center; gap: 6px; }
  .brand-mark { width: 16px; height: 16px; background: var(--brand-blue); }
  .brand-name { font-weight: 700; font-size: 20px; letter-spacing: 0.5px; color: var(--ink); line-height: 1; }
  .brand-sub { font-size: 9px; color: var(--brand-blue-light); margin-top: 2px; padding-left: 22px; }

  /* contact list */
  .contact { list-style: none; font-size: 6.5px; color: var(--muted); line-height: 1.55; }
  .contact li { display: flex; align-items: center; gap: 4px; }
  .contact li::before { content: ""; width: 4px; height: 4px; border-radius: 50%; background: var(--brand-blue-light); }

  /* tagline */
  .tagline { color: #fff; font-weight: 700; text-align: center; line-height: 0.95; }
  .tagline .big { display: block; }
  .tagline .small { font-size: 0.55em; font-weight: 400; }
  .tagline .tail { display: block; font-size: 0.7em; }

  /* business card front */
  .card-front { left: 60px; top: 60px; width: 252px; height: 144px; }
  .card-front .brand-block { left: 16px; top: 16px; }
  .card-front .brand-name { font-size: 16px; }
  .card-front .brand-mark { width: 13px; height: 13px; }
  .card-front .brand-sub { font-size: 7px; padding-left: 19px; }
  .card-front .holder { left: 16px; top: 66px; color: #fff; }
  .card-front .contact { left: 130px; top: 62px; font-size: 6px; color: #fff; }
  .card-front .contact li::before { background: #fff; }
  .holder-name { font-size: 8px; font-weight: 700; letter-spacing: 0.4px; }
  .holder-role { font-size: 6.5px; opacity: 0.85; }

  /* business card back */
  .card-back { left: 336px; top: 60px; width: 252px; height: 144px; background: var(--brand-blue); }
  .card-back .tagline { left: 0; right: 0; top: 38px; font-size: 19px; }
  .card-back .web { left: 0; right: 0; bottom: 14px; text-align: center; font-size: 7px; color: #dfe3f3; }

  /* envelope front */
  .envelope-front { left: 60px; top: 228px; width: 528px; height: 260px; }
  .envelope-front .brand-block { left: 26px; top: 24px; }
  .envelope-front .contact { left: 26px; top: 200px; }

  /* envelope back */
  .envelope-back { left: 60px; top: 508px; width: 528px; height: 260px; }
  .envelope-back .tagline { left: 0; right: 0; top: 196px; font-size: 20px; }

  /* letterhead */
  .letterhead { left: 636px; top: 40px; width: 504px; height: 720px; }
  .letterhead .brand-block { left: 40px; top: 38px; }
  .letterhead .contact { right: 40px; top: 92px; }
  .letter-body { left: 72px; top: 150px; width: 372px; font-size: 7.2px; line-height: 1.6; color: #555; }
  .letter-body p { margin-bottom: 8px; text-align: justify; }
  .letter-date { font-weight: 700; margin-bottom: 14px; }
  .signature-area { width: 80px; height: 22px; margin: 8px 0 2px; background: linear-gradient(90deg, rgba(68,86,159,0.25), rgba(68,86,159,0.08)); border-radius: 2px; }
  .sender-name { font-weight: 700; color: var(--ink); }
  .letterhead .tagline { left: 0; right: 0; top: 636px; font-size: 22px; }
</style>
</head>
<body>

<!-- Business card front -->
<section class="sheet card-front" aria-label="Business card front">
  <svg class="art" viewBox="0 0 252 144" preserveAspectRatio="none" aria-hidden="true">
    <polygon points="150,0 252,0 252,60" fill="var(--sweep)"/>
    <path d="M0,52 Q126,78 252,46 L252,144 L0,144Z" fill="var(--rule)"/>
    <path d="M0,56 Q126,82 252,50 L252,144 L0,144Z" fill="var(--brand-blue)"/>
  </svg>
  <div class="brand-block">
    <div class="brand"><span class="brand-mark"></span><span class="brand-name">BROVANIX</span></div>
    <div class="brand-sub">Advanced Cleaning Technologies</div>
  </div>
  <div class="holder">
    <div class="holder-name">CARDHOLDER NAME</div>
    <div class="holder-role">Designation</div>
  </div>
  <ul class="contact">
    <li>12 Harlow Street, Eastfield NSW 2150</li>
    <li>+61 2 5550 1234</li>
    <li>info@brovanix.com</li>
    <li>www.brovanix.com</li>
  </ul>
</section>

<!-- Business card back -->
<section class="sheet card-back" aria-label="Business card back">
  <svg class="art" viewBox="0 0 252 144" preserveAspectRatio="none" aria-hidden="true">
    <polygon points="0,0 110,0 0,90" fill="var(--brand-blue-light)" opacity="0.45"/>
    <polygon points="140,0 252,0 252,144 200,144" fill="var(--brand-blue-deep)" opacity="0.5"/>
    <polygon points="60,144 180,0 230,0 110,144" fill="var(--brand-blue-light)" opacity="0.25"/>
  </svg>
  <div class="tagline">
    <span class="big">Ultrasonic cleaning</span>
    <span class="big"><span class="small">and </span>High pressure</span>
    <span class="tail">cleaning machinery</span>
  </div>
  <div class="web">www.brovanix.com</div>
</section>

<!-- Envelope front -->
<section class="sheet envelope-front" aria-label="Envelope front">
  <svg class="art" viewBox="0 0 528 260" preserveAspectRatio="none" aria-hidden="true">
    <polygon points="200,260 420,0 528,0 528,60 360,260" fill="var(--sweep)"/>
    <polygon points="60,260 300,0 370,0 150,260" fill="var(--sweep-soft)"/>
  </svg>
  <div class="brand-block">
    <div class="brand"><span class="brand-mark"></span><span class="brand-name">BROVANIX</span></div>
    <div class="brand-sub">Advanced Cleaning Technologies</div>
  </div>
  <ul class="contact">
    <li>12 Harlow Street, Eastfield NSW 2150</li>
    <li>+61 2 5550 1234</li>
    <li>info@brovanix.com</li>
  </ul>
</section>

<!-- Envelope back -->
<section class="sheet envelope-back" aria-label="Envelope back">
  <svg class="art" viewBox="0 0 528 260" preserveAspectRatio="none" aria-hidden="true">
    <polyline points="0,30 20,14 508,14 528,30" fill="none" stroke="var(--rule)" stroke-width="1"/>
    <path d="M0,150 Q264,205 528,150 L528,260 L0,260Z" fill="var(--rule)"/>
    <path d="M0,158 Q264,213 528,158 L528,260 L0,260Z" fill="var(--brand-blue)"/>
    <path d="M0,200 Q264,250 528,196 L528,260 L0,260Z" fill="var(--brand-blue-deep)" opacity="0.35"/>
  </svg>
  <div class="tagline">
    <span class="big">Ultrasonic cleaning</span>
    <span class="big"><span class="small">and </span>High pressure</span>
    <span class="tail">cleaning machinery</span>
  </div>
</section>

<!-- Letterhead -->
<section class="sheet letterhead" aria-label="Letterhead">
  <svg class="art" viewBox="0 0 504 720" preserveAspectRatio="none" aria-hidden="true">
    <polygon points="0,430 380,140 504,140 504,190 90,520 0,520" fill="var(--sweep)"/>
    <polygon points="100,600 504,300 504,380 220,600" fill="var(--sweep-soft)"/>
    <path d="M0,560 Q252,640 504,560 L504,720 L0,720Z" fill="var(--rule)"/>
    <path d="M0,568 Q252,648 504,568 L504,720 L0,720Z" fill="var(--brand-blue)"/>
    <path d="M0,650 Q252,710 504,644 L504,720 L0,720Z" fill="var(--brand-blue-deep)" opacity="0.35"/>
  </svg>
  <div class="brand-block">
    <div class="brand"><span class="brand-mark"></span><span class="brand-name">BROVANIX</span></div>
    <div class="brand-sub">Advanced Cleaning Technologies</div>
  </div>
  <ul class="contact">
    <li>12 Harlow Street, Eastfield NSW 2150</li>
    <li>+61 2 5550 1234</li>
    <li>info@brovanix.com</li>
    <li>www.brovanix.com</li>
  </ul>
  <div class="letter-body">
    <p class="letter-date">Date: July 21 2013</p>
    <p>Dear Customer,</p>
    <p>Thank you for choosing our team for your cleaning needs. We supply ultrasonic tanks and high pressure washers for medical, automotive, mining and engineering sites. Each system is tested in our workshop before delivery, and our technicians stay on hand to support setup, training and servicing across the full life of the equipment.</p>
    <p>Our range covers compact benchtop units through to large industrial wash lines. We can tailor cycle times, tank sizes and detergents to suit the parts you clean, helping you cut labour, reduce waste water and keep critical components in service for longer.</p>
    <p>Please find our latest price list enclosed. If you would like a site visit or a live demonstration, contact our office and we will arrange a time that suits you.</p>
    <p>Regards,</p>
    <div class="signature-area" role="img" aria-label="Handwritten signature"></div>
    <div class="sender-name">SENDER NAME</div>
    <div>Designation</div>
  </div>
  <div class="tagline">
    <span class="big">Ultrasonic cleaning</span>
    <span class="big"><span class="small">and </span>High pressure</span>
    <span class="tail">cleaning machinery</span>
  </div>
</section>

</body>
</html>
```